Designing a Chocolate Bar's Package

We are a chocolate manufacturing company located in Lebanon. We produce chocolate on a wholesale level, and we are planning a new line of production at the moment.
We intend to be make small chocolate bars (about 30g) similar to the "Varmo Radiance" bar with several flavors. 2 flavors have been decided so far (Mint flavored dark chocolate and Plain dark chocolate).
The packaging material will be similar to varmo's package as well. It won't be a carton box. It'll be some sort of paper wrapping the entire bar. So I am looking for a design that has a unique and cool front and back look.
If only one design is to be prepared, please choose either the mint's flavor or the plain dark chocolate, and prepare the design accordingly.
Updates
Project Deadline Extended
Reason: I still have some time to begin the production. The new deadline,therefore, is the end of this month.
Target Market(s)
basically all chocolate lovers...
Industry/Entity Type
It Company
Requirements
Must have
- I will be uploading our logo. Please make sure to use it in the design.

```html
<!DOCTYPE html>
<html lang="en">
<head>
<meta charset="UTF-8">
<title>Chocolate Bar Wrapper – Back</title>
<link href="https://fonts.googleapis.com/css2?family=Arimo:wght@400;700&family=Satisfy&family=Lilita+One&display=swap" rel="stylesheet">
<style>
  :root {
    --page: #ffffff;
    --black: #000000;
    --cocoa: #2f2427;
    --teal: #174a56;
    --orange: #df5f38;
    --lime: #c6c83a;
    --script: #3f6c7a;
    --ink: #2b2226;
    --label-bg: #ffffff;
    --label-ink: #111111;
  }
  * { box-sizing: border-box; margin: 0; padding: 0; }
  html, body { width: 1200px; height: 900px; overflow: hidden; background: var(--page); }
  .canvas { position: relative; width: 1200px; height: 900px; }

  .wrapper-back {
    position: absolute; left: 14px; top: 20px; width: 386px; height: 850px;
    background: var(--page);
    box-shadow: 2px 3px 4px rgba(0,0,0,0.35);
  }
  .band-top { position: absolute; left: 0; top: 0; width: 100%; height: 28px; background: var(--black); }
  .band-bottom { position: absolute; left: 0; bottom: 0; width: 100%; height: 32px; background: var(--black); }
  .panel { position: absolute; left: 0; top: 28px; width: 100%; height: 564px; background: var(--cocoa); }
  .stripe { position: absolute; top: 0; height: 100%; }
  .stripe-teal { left: 0; width: 83px; background: var(--teal); }
  .stripe-orange { left: 83px; width: 11px; background: var(--orange); }
  .stripe-lime { left: 94px; width: 11px; background: var(--lime); }

  /* Nutrition label */
  .nutrition {
    position: absolute; left: 126px; top: 12px; width: 240px; height: 524px;
    background: var(--label-bg); color: var(--label-ink);
    font-family: "Arimo", Arial, sans-serif; padding: 0 6px;
  }
  .nf-title { font-size: 30.5px; font-weight: 700; line-height: 34px; margin-top: 2px; letter-spacing: -0.3px; }
  .nf-line { font-size: 12.5px; line-height: 13px; }
  .bar-thick { height: 9px; background: var(--label-ink); margin-top: 3px; }
  .bar-mid { height: 5px; background: var(--label-ink); }
  .nf-small-bold { font-size: 9px; font-weight: 700; line-height: 15px; border-bottom: 1px solid var(--label-ink); }
  .nf-row {
    display: flex; justify-content: space-between; align-items: center;
    height: 20.8px; font-size: 13px; border-bottom: 1px solid var(--label-ink);
  }
  .nf-row.cal { height: 22px; border-bottom: none; }
  .nf-row.indent { padding-left: 15px; }
  .nf-row.last { border-bottom: none; }
  .nf-row b { font-weight: 700; }
  .nf-dv { font-size: 9px; font-weight: 700; text-align: right; line-height: 14px; border-bottom: 1px solid var(--label-ink); }
  .nf-vit { display: flex; height: 20.5px; align-items: center; font-size: 12.5px; border-bottom: 1px solid var(--label-ink); }
  .nf-vit span:first-child { width: 110px; }
  .nf-foot { font-size: 9px; line-height: 10.5px; padding-top: 3px; }
  .nf-table { width: 100%; border-collapse: collapse; font-size: 8.6px; line-height: 11px; }
  .nf-table td { padding: 0; }
  .nf-table tr.head td { border-bottom: 1px solid var(--label-ink); }
  .nf-table tr.first td { padding-top: 2px; }
  .nf-table tr.end td { border-bottom: 1px solid var(--label-ink); padding-bottom: 2px; }
  .sub { padding-left: 6px !important; }
  .nf-cpg { font-size: 9px; line-height: 11px; padding-top: 3px; }
  .nf-cpg div:last-child { padding-left: 26px; }

  /* Story text */
  .story { position: absolute; left: 3px; top: 597px; width: 381px; text-align: justify; text-align-last: justify; }
  .story-lead { font-family: "Satisfy", cursive; font-size: 20px; line-height: 24px; color: var(--script); }
  .story-body {
    font-family: "Lilita One", sans-serif; font-size: 17.4px; line-height: 22.8px;
    color: var(--ink); text-transform: uppercase; letter-spacing: 0.2px;
  }
</style>
</head>
<body>
<div class="canvas">
  <div class="wrapper-back">
    <div class="band-top"></div>
    <div class="panel">
      <div class="stripe stripe-teal"></div>
      <div class="stripe stripe-orange"></div>
      <div class="stripe stripe-lime"></div>

      <section class="nutrition" aria-label="Nutrition Facts">
        <div class="nf-title">Nutrition Facts</div>
        <div class="nf-line">Serving Size 1/2 cup (about 82g)</div>
        <div class="nf-line">Servings Per Container 8</div>
        <div class="bar-thick"></div>
        <div class="nf-small-bold">Amount Per Serving</div>
        <div class="nf-row cal"><span><b>Calories</b> 200</span><span>Calories from Fat 130</span></div>
        <div class="bar-mid"></div>
        <div class="nf-dv">% Daily Value*</div>
        <div class="nf-row"><span><b>Total Fat</b> 14g</span><b>22%</b></div>
        <div class="nf-row indent"><span>Saturated Fat 9g</span><b>45%</b></div>
        <div class="nf-row indent"><span>Trans Fat 0g</span><span></span></div>
        <div class="nf-row"><span><b>Cholesterol</b> 55mg</span><b>18%</b></div>
        <div class="nf-row"><span><b>Sodium</b> 40mg</span><b>2%</b></div>
        <div class="nf-row"><span><b>Total Carbohydrate</b> 17g</span><b>6%</b></div>
        <div class="nf-row indent"><span>Dietary Fiber 1g</span><b>4%</b></div>
        <div class="nf-row indent"><span>Sugars 14g</span><span></span></div>
        <div class="nf-row last"><span><b>Protein</b> 3g</span><span></span></div>
        <div class="bar-thick" style="margin-top:0"></div>
        <div class="nf-vit"><span>Vitamin A 10%</span><span>•&nbsp; Vitamin C 0%</span></div>
        <div class="nf-vit"><span>Calcium 10%</span><span>•&nbsp; Iron 6%</span></div>
        <div class="nf-foot">*Percent Daily Values are based on a 2,000 calorie diet. Your daily values may be higher or lower depending on your calorie needs:</div>
        <table class="nf-table">
          <tr class="head"><td></td><td>Calories:</td><td>2,000</td><td>2,500</td></tr>
          <tr class="first"><td>Total Fat</td><td>Less than</td><td>65g</td><td>80g</td></tr>
          <tr><td class="sub">Saturated Fat</td><td>Less than</td><td>20g</td><td>25g</td></tr>
          <tr><td>Cholesterol</td><td>Less than</td><td>300mg</td><td>300 mg</td></tr>
          <tr><td>Sodium</td><td>Less than</td><td>2,400mg</td><td>2,400mg</td></tr>
          <tr><td>Total Carbohydrate</td><td></td><td>300g</td><td>375g</td></tr>
          <tr class="end"><td class="sub">Dietary Fiber</td><td></td><td>25g</td><td>30g</td></tr>
        </table>
        <div class="nf-cpg"><div>Calories per gram:</div><div>Fat 9 &nbsp;•&nbsp; Carbohydrate 4 &nbsp;•&nbsp; Protein 4</div></div>
      </section>
    </div>

    <div class="story">
      <p class="story-lead">At Corvello quality chocolate store,</p>
      <p class="story-body">Lorem ipsum dolor sit amet, consectetur adipiscing elit. Aenean sodales porta magna nec adipiscing. Donec nec feugiat mi. Integer elit sapien, ornare nec porta suscipit, pellentesque a massa. Suspendisse id ligula arcu. Maecenas tincidunt sollicitudin arcu sit amet pulvinar.</p>
    </div>

    <div class="band-bottom"></div>
  </div>
</div>
</body>
</html>
```